Software - upgrade look and feel

Brightwell Tallyworks is the worldwide distributor of the zLumio software application, which powers a loan strategy as described at www.brightwelltallyworks.com.The company has recently upgraded its image and website; and now seeks to give zLumio a much-needed face-lift.Using the screen shots of the existing application (2 x screens provided), recreate the screens in a modern and vibrant style that generates a feeling of professionalism and confidence.

Target Market(s)

Financial services industry and their clients.

Industry/Entity Type

Financial Service

Font styles to use
Other font styles liked:
• See our website at brightwelltallyworks.com - happy with this font, but open to ideas.

Colors

Designer to choose colors to be used in the design.

Requirements
Must have
• Existing fields, but perhaps more intuitive for the User.
Nice to have
• A less busy look that suggests an innovative software application.
Should not have
• Complication.

```html
<!DOCTYPE html>
<html lang="en">
<head>
<meta charset="utf-8">
<title>zLumio – Step 1 Client/Income</title>
<link rel="stylesheet" href="https://fonts.googleapis.com/css2?family=Arimo:wght@400;700&display=swap">
<style>
  :root{
    --teal:#1e7390;
    --teal-dark:#175e76;
    --teal-ghost:#185f78;
    --page:#f3f3f3;
    --tab-grey:#b3b3b3;
    --tab-text:#2a2a2a;
    --bar-grey:#b5b5b5;
    --bar-light:#e2e2e2;
    --ink:#1c1c1c;
    --link:#3b3fb6;
    --field-border:#2b2b2b;
    --select-blue:#2f67a6;
    --bubble:#a9a9a9;
    --connector:#a6a6a6;
    --step-green:#8cc47c;
    --step-grey:#b9b9b9;
    --icon-grey:#9c9c9c;
    --white:#ffffff;
  }
  *{box-sizing:border-box;margin:0;padding:0}
  html,body{width:1200px;height:1017px;overflow:hidden;background:var(--page)}
  body{font-family:"Arimo",Arial,sans-serif;color:var(--ink);position:relative}

  .app-header{position:absolute;left:0;top:0;width:1200px;height:135px;background:var(--teal);overflow:hidden}
  .brand-ghost{position:absolute;left:455px;top:-38px;font-size:150px;font-weight:700;color:var(--teal-ghost);letter-spacing:-2px;white-space:nowrap}
  .brand{position:absolute;left:44px;top:28px;font-size:52px;font-weight:700;color:var(--white);letter-spacing:1px}

  .step-tabs{position:absolute;left:6px;top:104px;width:1194px;height:31px}
  .tab{position:absolute;top:2px;height:29px;width:232px;background:var(--tab-grey);border-radius:8px 8px 0 0;font-size:14px;font-weight:700;color:var(--tab-text);text-align:center;line-height:30px}
  .tab.is-active{top:0;height:31px;background:var(--teal);color:var(--white);border:2px solid var(--white);border-bottom:none;line-height:27px;width:238px}

  .progress{position:absolute;left:0;top:178px;width:1200px;height:40px}
  .progress-line{position:absolute;top:18px;height:3px;background:var(--ink)}
  .progress-dot{position:absolute;top:2px;width:34px;height:34px;border-radius:50%;border:2px solid var(--ink);background:var(--step-grey);font-size:25px;text-align:center;line-height:30px;color:var(--ink)}
  .progress-dot.is-current{background:var(--step-green)}

  .section-bar{position:absolute;left:25px;top:240px;width:1146px;height:38px;border-radius:6px;background:linear-gradient(#ececec,#bdbdbd);border-bottom:3px solid #3a3a3a;box-shadow:0 1px 2px rgba(0,0,0,.25)}
  .section-title{position:absolute;left:14px;top:8px;font-size:25px;font-weight:700}
  .client-name{position:absolute;right:10px;top:4px;font-size:25px;font-weight:700}

  .label{position:absolute;left:34px;font-size:16px;white-space:nowrap}
  .link{color:var(--link);text-decoration:underline}
  .info{position:absolute;width:21px;height:21px;border-radius:50%;background:var(--icon-grey);color:var(--white);font-size:14px;font-weight:700;text-align:center;line-height:21px;font-family:Georgia,serif}
  .field{position:absolute;height:23px;background:var(--white);border:1.5px solid var(--field-border);border-radius:6px}
  .select-btn{position:absolute;right:1px;top:1px;width:18px;height:18px;border-radius:4px;background:var(--select-blue)}
  .select-btn svg{display:block}

  .callout{position:absolute;left:675px;top:418px;width:428px;height:150px;border-radius:50px;background:var(--bubble);text-align:center;font-size:12.5px;line-height:14px;padding:14px 30px 0}
  .callout b{font-weight:700}
  .connector{position:absolute;left:0;top:0}

  .divider{position:absolute;left:46px;width:1106px;height:8px;background:var(--bar-grey)}

  .col-head{position:absolute;top:718px;font-size:16px}
  .row-label{position:absolute;left:46px;font-size:16px}
  .add-client{position:absolute;left:598px;top:746px;width:28px;height:28px;border-radius:50%;background:var(--teal)}
  .tip{position:absolute;left:634px;top:699px;width:196px;height:32px;border-radius:9px;background:var(--bubble);font-size:16px;text-align:center;line-height:32px}

  .total-label{position:absolute;left:46px;font-size:16px;font-weight:700}

  .btn{position:absolute;top:973px;width:150px;height:23px;border-radius:3px;background:var(--teal);color:var(--white);font-size:16px;text-align:center;line-height:23px}
</style>
</head>
<body>

<header class="app-header">
  <div class="brand-ghost" aria-hidden="true">zLumio</div>
  <div class="brand">zLumio</div>
  <nav class="step-tabs">
    <div class="tab is-active" style="left:0">Step 1 - Client/Income</div>
    <div class="tab" style="left:240px">Step 2 - Expenses</div>
    <div class="tab" style="left:478px">Step 3 - Assets/Liabilities</div>
    <div class="tab" style="left:717px">Step 4 - Restructure</div>
    <div class="tab" style="left:956px">Step 5 - Calculate</div>
  </nav>
</header>

<div class="progress">
  <div class="progress-line" style="left:147px;width:160px"></div>
  <div class="progress-line" style="left:390px;width:160px"></div>
  <div class="progress-line" style="left:633px;width:160px"></div>
  <div class="progress-line" style="left:876px;width:160px"></div>
  <div class="progress-dot is-current" style="left:89px">1</div>
  <div class="progress-dot" style="left:332px">2</div>
  <div class="progress-dot" style="left:575px">3</div>
  <div class="progress-dot" style="left:818px">4</div>
  <div class="progress-dot" style="left:1060px">5</div>
</div>

<div class="section-bar">
  <div class="section-title">Client Details</div>
  <div class="client-name">Peter &amp; Ann Hale</div>
</div>

<!-- Client details form -->
<div class="label" style="top:310px">View</div>
<div class="info" style="left:195px;top:308px">i</div>
<div class="field" style="left:224px;top:307px;width:225px"><div class="select-btn"><svg width="18" height="18" viewBox="0 0 18 18"><path d="M5 7l4-3 4 3M5 11l4 3 4-3" fill="none" stroke="#fff" stroke-width="1.6"/></svg></div></div>

<div class="label" style="top:340px">Title</div>
<div class="info" style="left:195px;top:338px">i</div>
<div class="field" style="left:224px;top:337px;width:87px"><div class="select-btn"><svg width="18" height="18" viewBox="0 0 18 18"><path d="M5 7l4-3 4 3M5 11l4 3 4-3" fill="none" stroke="#fff" stroke-width="1.6"/></svg></div></div>
<div class="label link" style="left:317px;top:339px">Additional Details</div>

<div class="label" style="top:368px">Family Name</div>
<div class="info" style="left:195px;top:366px">i</div>
<div class="field" style="left:224px;top:366px;width:225px"></div>

<div class="label" style="top:400px">First Name</div>
<div class="info" style="left:195px;top:398px">i</div>
<div class="field" style="left:224px;top:397px;width:225px"></div>

<div class="label" style="top:430px">File No.</div>
<div class="info" style="left:195px;top:428px">i</div>
<div class="field" style="left:224px;top:427px;width:225px"></div>

<div class="label" style="top:460px">Email</div>
<div class="info" style="left:195px;top:458px">i</div>
<div class="field" style="left:224px;top:458px;width:225px"></div>

<div class="label link" style="top:489px">Loan Writer User</div>
<div class="field" style="left:224px;top:487px;width:225px"><div class="select-btn"><svg width="18" height="18" viewBox="0 0 18 18"><path d="M5 7l4-3 4 3M5 11l4 3 4-3" fill="none" stroke="#fff" stroke-width="1.6"/></svg></div></div>

<div class="label link" style="top:519px">CS Officer</div>
<div class="field" style="left:224px;top:517px;width:225px"><div class="select-btn"><svg width="18" height="18" viewBox="0 0 18 18"><path d="M5 7l4-3 4 3M5 11l4 3 4-3" fill="none" stroke="#fff" stroke-width="1.6"/></svg></div></div>

<div class="label" style="top:549px">Simulatiom Purpose</div>
<div class="field" style="left:224px;top:547px;width:225px"><div class="select-btn"><svg width="18" height="18" viewBox="0 0 18 18"><path d="M5 7l4-3 4 3M5 11l4 3 4-3" fill="none" stroke="#fff" stroke-width="1.6"/></svg></div></div>

<div class="label link" style="top:576px">Statistics</div>
<div class="label link" style="left:225px;top:576px">Send to Pending Tray</div>
<div class="label link" style="top:600px">Minimisation Strategy</div>
<div class="label link" style="left:225px;top:600px">LFBA Guidelines</div>

<!-- Help callout -->
<svg class="connector" width="1200" height="1017" aria-hidden="true">
  <polyline points="905,566 905,647 201,647 201,738" fill="none" stroke="var(--connector)" stroke-width="3"/>
  <path d="M196 736 L206 736 L201 744 Z" fill="var(--connector)"/>
</svg>
<div class="callout">
  <b>Please Enter the names of Client 1 and Client 2 ( if applicable),then enter after tax wage or salary per frequency of payment .</b> Note: Unless you enter the name of Client 1, no income will be saved for client 1. Unless you enter the name of Client 2, No income may be entered for Client 2.
</div>

<div class="divider" style="top:668px"></div>

<!-- Income -->
<div class="col-head" style="left:239px">Net (After Tax)</div>
<div class="col-head" style="left:416px">Freq. of Payment</div>

<div class="row-label" style="top:750px">Client 1</div>
<div class="info" style="left:186px;top:748px">i</div>
<div class="field" style="left:214px;top:747px;width:162px"></div>
<div class="field" style="left:382px;top:747px;width:203px"><div class="select-btn"><svg width="18" height="18" viewBox="0 0 18 18"><path d="M5 7l4-3 4 3M5 11l4 3 4-3" fill="none" stroke="#fff" stroke-width="1.6"/></svg></div></div>
<div class="add-client"><svg width="28" height="28" viewBox="0 0 28 28"><path d="M14 7v14M7 14h14" stroke="#fff" stroke-width="3"/></svg></div>
<svg class="connector" width="1200" height="1017" aria-hidden="true"><path d="M636 742 L652 728 L672 728 Z" fill="var(--bubble)"/></svg>
<div class="tip">Click here to add client 2</div>

<div class="row-label" style="top:782px">Client 2</div>
<div class="field" style="left:214px;top:779px;width:162px"></div>
<div class="field" style="left:382px;top:779px;width:203px"><div class="select-btn"><svg width="18" height="18" viewBox="0 0 18 18"><path d="M5 7l4-3 4 3M5 11l4 3 4-3" fill="none" stroke="#fff" stroke-width="1.6"/></svg></div></div>

<div class="divider" style="top:845px"></div>

<!-- Totals -->
<div class="total-label" style="top:901px">Client 1 Affter Tax Income</div>
<div class="field" style="left:291px;top:893px;width:188px"></div>
<div class="total-label" style="top:931px">Combined After Tax Income</div>
<div class="field" style="left:291px;top:923px;width:188px"></div>

<div class="btn" style="left:767px">Save</div>
<div class="btn" style="left:923px">Cancel</div>

</body>
</html>
```